Harbor of Separation Website Design

The primary objectives of this website is lead generation, create authority and enhance trust factor so that potential clients utilize Harbor of Separation services.

In an effort to provide prospects with a comprehensive explanation of the company’s services, Harbor of Separation will be creating a new website to provide, a user-friendly experience that will lead a person onto the right pathway where they will find tailored information depending on the stage they are in: Thinking of Divorce, Ready to Move Forward, and Recently Divorced.

Visitors will land on the homepage, which will give them the opportunity to select from the three types of personas shown. Messaging will be written specifically for each persona type, a lead-gen form will be present throughout the entire site, and a free downloadable form will be provided to them.

Once the lead gen form is submitted, information will be sent to Harbor of Separation consultant, who will follow up with the prospect.

Social Integration with website continue to prove Harbor of Separation authority and expertise.

Target Market(s)

Individuals who are considering or our in the process of divorce find themselves in a state of trying to make sense of it all. They lack the knowledge they need concerning the divorce process. Both men and women are typically scared of the unknown and financial loss. Due to the emotional stress they hire an attorney quickly that may not be suitable to their personality and/or situation.

Both men and women need an unbiased and informed partner that can guide them in the right direction. Time is their most precious commodity; making costly mistakes might ruin their financial situation, enhance their stress levels and prolong the divorce process. Both parties are looking for the right answers, the right professional divorce team, i.e. lawyer, mediator, financial planner, etc. to help them get their lives back in order.

Demographics
• Men and Women
• Ages 36 to 55
• Income: 80K+ per person or $150K+ combined
• Working Professionals: dentist, managers, creative directors, bankers, etc.

Industry/Entity Type

It Company

Requirements
Must have
• Visual Feeling
• The look and feel should represent a feeling of trust and reliability.
• Use colors from the logo.
• Please select images from Q-Frame Images
• Please refer to wireframes to see where images should be placed
• Calls To Action should stand out on each page.

Use the new logo Harbor of Separation Logo and tagline: Answers, Referrals, Support.

Please use the following URL: www.harborofseparation-example.com

```html
<!DOCTYPE html>
<html lang="en">
<head>
<meta charset="utf-8">
<title>Harbor of Separation</title>
<link href="https://fonts.googleapis.com/css2?family=Questrial&family=Arimo:wght@400;700&display=swap" rel="stylesheet">
<style>
:root{
  --blue:#4a7fc1;
  --blue-dark:#3b6fae;
  --green:#5a9a32;
  --green-box:rgba(98,165,52,.88);
  --gray-box:rgba(110,110,110,.82);
  --blue-box:rgba(74,127,193,.9);
  --white-box:rgba(255,255,255,.82);
  --panel:rgba(78,74,70,.82);
  --yellow:#e3c417;
  --text:#333;
  --logo-gray:#555;
}
*{margin:0;padding:0;box-sizing:border-box}
html,body{width:755px;height:1200px;overflow:hidden;background:#fff}
body{position:relative;font-family:"Arimo",Arial,sans-serif;color:var(--text)}
.abs{position:absolute}
.brand{left:13px;top:13px;display:flex;align-items:center;gap:8px}
.brand-mark{width:36px;height:36px;border-radius:50%;background:var(--green)}
.brand-name{font-family:"Questrial",sans-serif;font-size:16px;font-weight:bold;color:var(--logo-gray);text-transform:uppercase;letter-spacing:.2px}
.call{right:12px;top:6px;text-align:right;font-family:"Questrial",sans-serif;color:var(--blue)}
.call-label{font-size:18px;font-weight:bold;line-height:20px}
.call-number{font-size:14px}
.share{right:10px;top:48px;width:102px;height:13px;border:1px solid #ccc;border-radius:2px;font-size:7px;display:flex;align-items:center;gap:4px;padding:0 3px;color:#333;letter-spacing:.5px}
.share .dot{width:7px;height:7px;background:#e04a2a}
.share .sq{width:6px;height:6px;background:#6b88b8;margin-left:auto}
.share .sq+.sq{margin-left:0}
.nav{left:8px;top:65px;width:741px;height:30px;background:var(--green);display:flex;align-items:center;padding-left:14px}
.nav a{font-family:"Questrial",sans-serif;color:#fff;font-size:10.5px;text-decoration:none;margin-right:45px}
.hero{left:8px;top:98px;width:741px;height:440px;background:linear-gradient(100deg,#6d6358 0%,#9a8a78 35%,#c2a58b 55%,#8f7b6b 75%,#5f5750 100%)}
.tile{width:244px;height:109px;font-family:"Questrial",sans-serif}
.tile-title{position:absolute;left:0;right:0;top:44px;text-align:center;font-size:14px}
.tile-link{position:absolute;right:24px;bottom:13px;font-size:13.5px;font-weight:bold;display:flex;align-items:center;gap:4px}
.tile-link svg{width:9px;height:10px}
.t-blue{left:4px;top:138px;background:var(--blue-box);color:#fff}
.t-white{left:195px;top:242px;background:var(--white-box);color:var(--blue)}
.t-gray{left:4px;top:340px;background:var(--gray-box);color:#fff}
.t-green{left:149px;top:440px;background:var(--green-box);color:#fff}
.panel{left:426px;top:129px;width:312px;height:301px;background:var(--panel)}
.panel-head{position:absolute;left:0;right:0;top:44px;text-align:center;color:#fff;font-family:"Questrial",sans-serif;font-weight:bold;font-size:15px;line-height:19px}
.cta-arrow{left:459px;top:371px}
.cta{left:493px;top:362px;width:234px;height:45px;background:var(--yellow);border:1px solid #f0dc62;color:#fff;font-family:"Questrial",sans-serif;font-weight:bold;font-size:13.5px;display:flex;align-items:center;justify-content:center}
.copy{left:9px;top:574px;width:740px;font-size:10.2px;line-height:13px;color:#444}
.copy p{margin-bottom:13px}
.seen{left:12px;top:826px;font-size:13px;color:#444}
.badge{top:862px;width:106px;height:106px;background:#1f74bd}
.b1{left:33px;border-radius:50%}
.b2{left:206px;background:#6a6a6a;border-radius:10px}
.b3{left:392px;border-radius:50%;background:#111}
.b4{left:550px;width:162px;height:72px;top:878px;background:#1e3d91}
.footer{left:8px;top:1010px;width:741px;height:190px;background:var(--blue);color:#fff}
.fcol{position:absolute;top:14px}
.fcol h3{font-family:"Questrial",sans-serif;font-weight:normal;font-size:14px;line-height:17px;margin-bottom:10px}
.fcol ul{list-style:none;font-size:9px;line-height:12.4px}
.fsmall{font-size:9px;line-height:11px}
.quote-icon{position:absolute;left:0;top:28px}
.input{width:163px;height:18px;background:#fff;color:#4a7fc1;font-size:8.5px;padding:4px 7px;margin-bottom:5px}
.signup{position:absolute;left:89px;top:99px;width:73px;height:23px;background:#8fb0de;font-size:10px;font-weight:bold;display:flex;align-items:center;justify-content:center}
.follow{position:absolute;left:51px;top:148px;display:flex;align-items:center;gap:8px;font-size:10px}
.social{width:25px;height:25px;background:#9bb7df}
</style>
</head>
<body>
<header>
  <div class="abs brand"><span class="brand-mark"></span><span class="brand-name">Harbor of Separation</span></div>
  <div class="abs call"><div class="call-label">Call Us</div><div class="call-number">555.014.2290</div></div>
  <div class="abs share"><span class="dot"></span>SHARE<span class="sq"></span><span class="sq"></span><span class="sq"></span></div>
  <nav class="abs nav"><a>ABOUT US</a><a>SERVICES</a><a>RESOURCES</a><a>TAKE CONTROL</a><a>CONTACT US</a></nav>
</header>

<section class="abs hero" role="img" aria-label="Photo of a worried couple sitting apart at a table"></section>

<div class="abs tile t-blue"><div class="tile-title">Thinking of Divorce?</div><div class="tile-link"><svg viewBox="0 0 9 10"><path d="M0 0L9 5L0 10Z" fill="currentColor"/></svg>Learn More</div></div>
<div class="abs tile t-white"><div class="tile-title">Need to Do Something</div><div class="tile-link"><svg viewBox="0 0 9 10"><path d="M0 0L9 5L0 10Z" fill="currentColor"/></svg>Learn More</div></div>
<div class="abs tile t-gray"><div class="tile-title">Recently Divorce?</div><div class="tile-link"><svg viewBox="0 0 9 10"><path d="M0 0L9 5L0 10Z" fill="currentColor"/></svg>Learn More</div></div>
<div class="abs tile t-green"><div class="tile-title">Financial Help</div><div class="tile-link"><svg viewBox="0 0 9 10"><path d="M0 0L9 5L0 10Z" fill="currentColor"/></svg>Learn More</div></div>

<div class="abs panel"><div class="panel-head">Take the “mystery” our of divorce.<br>Find out what you need to know!</div></div>
<svg class="abs cta-arrow" width="26" height="30" viewBox="0 0 26 30"><path d="M0 7H12V0L26 15L12 30V23H0Z" fill="#e3c417"/></svg>
<div class="abs cta">Schedule your Free consultation</div>

<main class="abs copy">
  <p>Lorem ipsum dolor sit amet, consectetur adipisicing elit, sed do eiusmod tempor incididunt ut labore et dolore magna aliqua. Ut enim ad minim veniam, quis nostrud exercitation ullamco laboris nisi ut aliquip ex ea commodo consequat. Duis aute irure dolor in reprehenderit in voluptate velit esse cillum dolore eu fugiat nulla pariatur. Excepteur sint occaecat cupidatat non proident, sunt in culpa qui officia deserunt mollit anim id est laborum.</p>
  <p>Sed ut perspiciatis, unde omnis iste natus error sit voluptatem accusantium doloremque laudantium, totam rem aperiam eaque ipsa, quae ab illo inventore veritatis et quasi architecto beatae vitae dicta sunt, explicabo. Nemo enim ipsam voluptatem, quia voluptas sit, aspernatur aut odit aut fugit, sed quia consequuntur magni dolores eos, qui ratione voluptatem sequi nesciunt, neque porro quisquam est, qui dolorem ipsum, quia dolor sit amet, consectetur, adipisci[ng] velit, sed quia non numquam [do] eius modi tempora inci[di]dunt, ut labore et dolore magnam aliquam quaerat voluptatem. Ut enim ad minima veniam, quis nostrum exercitationem ullam corporis suscipit laboriosam, nisi ut aliquid ex ea commodi consequatur? Quis autem vel eum iure reprehenderit, qui in ea voluptate velit esse, quam nihil molestiae consequatur, vel illum, qui dolorem eum fugiat, quo voluptas nulla pariatur?</p>
  <p>At vero eos et accusamus et iusto odio dignissimos ducimus, qui blanditiis praesentium voluptatum deleniti atque corrupti, quos dolores et quas molestias excepturi sint, obcaecati cupiditate non provident, similique sunt in culpa, qui officia deserunt mollitia animi, id est laborum et dolorum fuga. Et harum quidem rerum facilis est et expedita distinctio. Nam libero tempore, cum soluta nobis est eligendi optio, cumque nihil impedit, quo minus id, quod maxime placeat, facere possimus, omnis voluptas assumenda est, omnis dolor repellendus. Temporibus autem quibusdam et aut officiis debitis aut rerum necessitatibus saepe eveniet, ut et voluptates repudiandae sint et molestiae non recusandae. Itaque earum rerum hic tenetur a sapiente delectus, ut aut reiciendis voluptatibus maiores alias consequatur aut perferendis doloribus asperiores</p>
</main>

<div class="abs seen">As Seen on:</div>
<div class="abs badge b1" aria-label="Media badge"></div>
<div class="abs badge b2" aria-label="Media badge"></div>
<div class="abs badge b3" aria-label="Media badge"></div>
<div class="abs badge b4" aria-label="Media badge"></div>

<footer class="abs footer">
  <div class="fcol" style="left:19px">
    <h3>Quick Links</h3>
    <ul><li>About Us</li><li>Services</li><li>Testimonials</li><li>Resources</li><li>Take Control</li><li>Contact Us</li><li>Privacy Policy</li><li>Terms</li><li>Disclaimers</li></ul>
  </div>
  <div class="fcol" style="left:131px;width:210px">
    <h3>What People are Saying</h3>
    <svg class="quote-icon" width="34" height="30" viewBox="0 0 34 30"><ellipse cx="15" cy="12" rx="14" ry="11" fill="none" stroke="#cfdcf0" stroke-width="2"/><ellipse cx="24" cy="20" rx="9" ry="7" fill="#cfdcf0"/><text x="8" y="17" font-size="14" fill="#cfdcf0" font-family="Arimo,sans-serif">“</text></svg>
    <div style="padding-left:42px">
      <p class="fsmall">Lorem ipsum dolor sit amet, consectetur adipisicing elit, sed do eiusmod tempor incididunt ut labore et dolore magna aliqua. Ut enim ad minim veniam, quis nostrud exercitation ullamco</p>
      <p style="font-size:10px;margin-top:12px">- Dana Whitfield</p>
    </div>
  </div>
  <div class="fcol fsmall" style="left:380px">
    <h3>Get In Touch</h3>
    <p>Copyright 2013</p>
    <p style="margin-top:11px">Tidewell Partners<br>4120 Lantern Bay Road Ste 210<br>Port Elling, Coastland 40718</p>
    <p style="margin-top:11px">555.014.2290</p>
  </div>
  <div class="fcol" style="left:546px;width:170px;height:176px">
    <h3>Tidewell Newsletter<br>Educate Your Selft</h3>
    <div class="input">full name</div>
    <div class="input">email</div>
    <div class="signup">Sign Up</div>
    <div class="follow">Follow Us <span class="social"></span><span class="social"></span></div>
  </div>
</footer>
</body>
</html>
```